Rivolex.com Trucking Company Website

Need a website designed (no content) for a trucking company, specializing in trucking of ocean containers (intermodal Trucking). Heavy emphasis on technology, using latest technology, providing unabated visibility and realtime information.
clean minimalist industrial website
example:
https://www.bramtiq.com/

Target Market(s)

Professional Business Consumer corporate and small business

Industry/Entity Type

Trucking Company

Number of Pages Required

5+ page

Requirements
Must have
• Industrial Design, simple informative, for a busy professional to view and get the necessary information with out the distractions.
• Blog Page
• Client Log-In on the front page
• Technology page - showing our intensive investments in technology
Nice to have
• If ANY images included, MUST be USA related. Example if include an image of a truck, ensure its a USA model. Do the research.
• included our business card for sample of Logo
• Doesnt not have to be the same color schemes.
Should not have
• moving images

```html
<!DOCTYPE html>
<html lang="en">
<head>
<meta charset="utf-8">
<title>Rivolex Consulting — Intermodal Trucking</title>
<link href="https://fonts.googleapis.com/css2?family=Raleway:wght@400;500;600;700&family=Lato:wght@400;700&display=swap" rel="stylesheet">
<style>
  :root {
    --brand-blue: #1a5ea8;
    --ink: #222;
    --ink-soft: #333;
    --white: #fff;
    --hero-dark: #2a2d33;
    --hero-mid: #565a61;
    --menu-line: #dcdcdc;
    --menu-hover: #e9e9e9;
    --section-bg: #f1f4f7;
    --rule: #c9ccd0;
    --footer: #050505;
  }
  * { box-sizing: border-box; margin: 0; padding: 0; }
  html, body { width: 1187px; height: 1200px; overflow: hidden; }
  body { position: relative; font-family: "Lato", sans-serif; color: var(--ink); background: var(--white); }

  .hero { position: absolute; left: 0; top: 0; width: 1187px; height: 645px; overflow: hidden; }
  .hero-photo {
    position: absolute; inset: 0;
    background:
      radial-gradient(ellipse 300px 260px at 480px 330px, rgba(215,190,170,.55), transparent 70%),
      radial-gradient(ellipse 520px 360px at 620px 330px, rgba(150,160,175,.45), transparent 70%),
      linear-gradient(90deg, var(--hero-dark), var(--hero-mid) 45%, var(--hero-dark));
  }
  .call-now { position: absolute; right: 103px; top: 9px; color: var(--white); font-family: "Lato", sans-serif; font-weight: 700; font-size: 17px; display: flex; align-items: center; gap: 8px; }
  .call-now svg { opacity: .5; }

  .site-header { position: absolute; left: 97px; top: 42px; width: 992px; height: 94px; background: var(--white); border-radius: 12px; }
  .brand { position: absolute; left: 22px; top: 28px; font-family: "Raleway", sans-serif; font-weight: 700; font-size: 30px; color: var(--brand-blue); letter-spacing: 1px; }
  .client-login { position: absolute; left: 745px; top: 32px; display: flex; align-items: center; gap: 8px; font-family: "Raleway", sans-serif; font-size: 16px; color: var(--ink); }
  .menu-toggle { position: absolute; left: 920px; top: 23px; width: 44px; height: 50px; border: 2px solid #111; border-bottom: none; border-radius: 4px 4px 0 0; background: var(--white); z-index: 3; }
  .menu-toggle span { position: absolute; left: 8px; width: 28px; height: 2px; background: #111; }

  .main-menu { position: absolute; left: 857px; top: 106px; width: 204px; height: 360px; overflow: hidden; background: var(--white); border: 2px solid #111; border-radius: 0 0 5px 5px; z-index: 2; list-style: none; padding: 5px 12px 0 10px; }
  .main-menu li { font-family: "Raleway", sans-serif; font-size: 13.5px; color: var(--ink-soft); border-bottom: 1px dotted var(--menu-line); height: 31.5px; line-height: 31.5px; white-space: nowrap; }
  .main-menu li:last-child { border-bottom: none; }
  .main-menu li.active { background: var(--menu-hover); margin: 0 -12px 0 -10px; padding-left: 10px; font-weight: 600; color: var(--ink); }
  .main-menu li.active::after { content: ""; display: inline-block; margin-left: 4px; border: 4px solid transparent; border-top-color: #222; vertical-align: -1px; }

  .sub-menu { position: absolute; left: 680px; top: 244px; width: 177px; height: 71px; background: var(--menu-hover); border: 1px solid #999; list-style: none; padding: 0 10px 0 16px; z-index: 2; }
  .sub-menu li { font-family: "Raleway", sans-serif; font-size: 13.5px; color: var(--ink-soft); height: 34.5px; line-height: 34.5px; border-bottom: 1px solid #d4d4d4; }
  .sub-menu li:last-child { border-bottom: none; }

  .tagline { position: absolute; left: 468px; top: 557px; width: 622px; height: 66px; background: rgba(5,5,5,.88); border: 1px solid #777; color: var(--white); font-family: "Raleway", sans-serif; font-weight: 700; font-size: 31px; line-height: 64px; text-align: center; }

  .services-section { position: absolute; left: 0; top: 645px; width: 1187px; height: 504px; background: linear-gradient(90deg, #fbfbfc, var(--section-bg)); }
  .intro { position: absolute; left: 90px; top: 140px; width: 390px; text-align: center; }
  .intro-brand { font-family: "Raleway", sans-serif; font-weight: 700; font-size: 50px; line-height: 1.05; color: var(--brand-blue); }
  .intro-text { margin-top: 22px; font-family: "Lato", sans-serif; font-size: 22px; line-height: 31px; color: #333; }

  .service-list { position: absolute; left: 574px; top: 42px; width: 520px; height: 423px; border-left: 2px solid var(--rule); list-style: none; }
  .service { position: absolute; left: -2px; width: 520px; height: 85px; border-left: 2px solid var(--brand-blue); padding-left: 22px; }
  .service::before { content: ""; position: absolute; left: -1px; top: 36px; border: 5px solid transparent; border-left-color: var(--brand-blue); }
  .service-head { display: flex; align-items: center; gap: 18px; height: 38px; }
  .service-head h2 { font-family: "Raleway", sans-serif; font-weight: 600; font-size: 20px; color: #2c2c2c; }
  .service p { font-size: 13.7px; line-height: 19px; color: #222; margin-top: 2px; }

  .site-footer { position: absolute; left: 0; top: 1149px; width: 1187px; height: 51px; background: var(--footer); color: var(--white); font-size: 13.5px; text-align: center; line-height: 51px; }
</style>
</head>
<body>
  <section class="hero">
    <div class="hero-photo" role="img" aria-label="Businessman touching a map of the United States dotted with container trucks"></div>

    <div class="call-now">
      <svg width="14" height="14" viewBox="0 0 24 24"><path fill="#fff" d="M6.6 10.8a15 15 0 0 0 6.6 6.6l2.2-2.2a1 1 0 0 1 1-.25 11.4 11.4 0 0 0 3.6.57 1 1 0 0 1 1 1V20a1 1 0 0 1-1 1A17 17 0 0 1 3 4a1 1 0 0 1 1-1h3.5a1 1 0 0 1 1 1c0 1.25.2 2.45.57 3.57a1 1 0 0 1-.25 1z"/></svg>
      Call Now : 555-014-2290
    </div>

    <header class="site-header">
      <div class="brand">Rivolex Consulting</div>
      <div class="client-login">
        <svg width="30" height="28" viewBox="0 0 30 28"><circle cx="11" cy="7" r="6" fill="#111"/><path d="M0 27c0-7 5-11 11-11s11 4 11 11z" fill="#111"/><circle cx="23" cy="21" r="6" fill="#fff" stroke="#111" stroke-width="2"/><circle cx="21" cy="21" r="1.6" fill="#111"/><path d="M22 21h5" stroke="#111" stroke-width="1.6"/></svg>
        Client Log-In
      </div>
      <div class="menu-toggle"><span style="top:16px"></span><span style="top:22px"></span><span style="top:28px"></span></div>
    </header>

    <ul class="main-menu">
      <li>About Rivolex</li>
      <li>Who We Are</li>
      <li>Technology</li>
      <li>Freight Quote</li>
      <li class="active">Apply for a Driver position</li>
      <li>Environment</li>
      <li>Industry News</li>
      <li>Press Release</li>
      <li>How It Works</li>
      <li>Blog</li>
      <li>FAQ's</li>
    </ul>
    <ul class="sub-menu">
      <li>Technology</li>
      <li>Freight Quote</li>
    </ul>

    <div class="tagline">We Are A Technology Driven Company</div>
  </section>

  <section class="services-section">
    <div class="intro">
      <div class="intro-brand">Rivolex Consulting</div>
      <p class="intro-text">We Are A Trucking Business Specializing In Trucking Of Ocean Containers</p>
    </div>

    <ul class="service-list">
      <li class="service" style="top:32px">
        <div class="service-head">
          <svg width="30" height="36" viewBox="0 0 30 36"><rect x="3" y="4" width="24" height="24" rx="4" fill="none" stroke="#333" stroke-width="2.4"/><rect x="7" y="8" width="16" height="7" fill="#333"/><circle cx="9" cy="22" r="2" fill="#333"/><circle cx="21" cy="22" r="2" fill="#333"/><rect x="5" y="28" width="5" height="6" fill="#333"/><rect x="20" y="28" width="5" height="6" fill="#333"/></svg>
          <h2>Intermodal Trucking</h2>
        </div>
        <p>Lorem ipsum dolor sit amet, consectetur adipiscing elit, sed do eiusmod tempor incididunt ut labore et dolore magna aliqua. Ut enim ad minim veniam, quis nostrud</p>
      </li>
      <li class="service" style="top:159px">
        <div class="service-head">
          <svg width="40" height="32" viewBox="0 0 40 32"><rect x="1" y="2" width="26" height="20" rx="2" fill="#333"/><path d="M27 9h7l5 7v9H27z" fill="#333"/><circle cx="9" cy="26" r="4.5" fill="#333" stroke="#fff" stroke-width="1.5"/><circle cx="31" cy="26" r="4.5" fill="#333" stroke="#fff" stroke-width="1.5"/><text x="3" y="16" font-family="Lato, sans-serif" font-weight="700" font-size="10" fill="#fff">LTL</text></svg>
          <h2>LTL</h2>
        </div>
        <p>Lorem ipsum dolor sit amet, consectetur adipiscing elit, sed do eiusmod tempor incididunt ut labore et dolore magna aliqua. Ut enim ad minim veniam, quis nostrud</p>
      </li>
      <li class="service" style="top:286px">
        <div class="service-head">
          <svg width="34" height="32" viewBox="0 0 34 32"><path d="M1 10 17 2l16 8v21H1z" fill="#333"/><rect x="6" y="14" width="22" height="17" fill="#fff"/><rect x="8" y="20" width="6" height="5" fill="#333"/><rect x="15" y="20" width="6" height="5" fill="#333"/><rect x="8" y="26" width="6" height="5" fill="#333"/><rect x="15" y="26" width="6" height="5" fill="#333"/><rect x="22" y="26" width="4" height="5" fill="#333"/></svg>
          <h2>Warehousing</h2>
        </div>
        <p>Lorem ipsum dolor sit amet, consectetur adipiscing elit, sed do eiusmod tempor incididunt ut labore et dolore magna aliqua. Ut enim ad minim veniam, quis nostrud</p>
      </li>
    </ul>
  </section>

  <footer class="site-footer">Copyright © 2017&nbsp; Rivolex Consulting&nbsp; I&nbsp; All Rights Reserved.</footer>
</body>
</html>
```